Business card for Financial Technology company

Hello! We'd like to create business cards for 4 members of our company. Our company is a financial technology business that provides funding for businesses. We want to give it a VC (venture captal) look and feel. Clean, fresh and minimal but with a flair of artistry. I'll include some samples of cards we like. It would be great if the back of the card was artistic (see sample files 1 and 2) and the front of the card was the business info. The name of the company is Q7 Funding.

```html
<!DOCTYPE html>
<html lang="en">
<head>
<meta charset="utf-8">
<title>Q7 Funding — Business Card</title>
<link rel="stylesheet" href="https://fonts.googleapis.com/css2?family=Kanit:wght@300;400;500;600&display=swap">
<style>
  :root {
    --canvas: #e6e6e8;
    --card-white: #ffffff;
    --magenta: #d90f8c;
    --magenta-light: #e2469f;
    --magenta-deep: #8e1a64;
    --plum: #7a1656;
    --band: #ad1f8a;
    --yellow: #f6bb18;
    --navy: #0f4f7d;
    --pink: #ec4f74;
    --orange: #f28a2e;
    --green: #14914a;
    --purple: #6a2c91;
    --ink: #1d1d1f;
  }
  * { box-sizing: border-box; margin: 0; padding: 0; }
  html, body { width: 1200px; height: 1200px; overflow: hidden; }
  body {
    background: var(--canvas);
    font-family: "Kanit", sans-serif;
    position: relative;
  }
  .card {
    position: absolute;
    top: 232px;
    width: 420px;
    height: 736px;
    overflow: hidden;
    box-shadow: 0 10px 30px rgba(0,0,0,0.18);
  }
  .card--front { left: 150px; background: var(--card-white); }
  .card--back { left: 630px; background: var(--magenta); }

  /* Front */
  .brand-mark {
    position: absolute;
    top: 176px;
    left: 0;
    width: 100%;
    display: flex;
    align-items: center;
    justify-content: center;
    gap: 14px;
  }
  .brand-mark__dot { width: 24px; height: 24px; background: var(--magenta); }
  .brand-mark__name {
    font-size: 46px;
    font-weight: 600;
    line-height: 1;
    color: var(--magenta);
    letter-spacing: 0.5px;
  }
  .timeline {
    position: absolute;
    left: 66px;
    top: 410px;
    width: 2px;
    height: 220px;
    background: var(--orange);
  }
  .hex { position: absolute; display: block; }
  .hex--person { left: 44px; top: 370px; }
  .person-name {
    position: absolute;
    left: 104px;
    top: 364px;
    font-size: 36px;
    font-weight: 600;
    line-height: 1;
    letter-spacing: 1px;
    white-space: nowrap;
  }
  .person-name__first { color: var(--yellow); }
  .person-name__last { color: var(--navy); }
  .person-title {
    position: absolute;
    left: 104px;
    top: 404px;
    font-size: 17px;
    font-weight: 300;
    line-height: 1.2;
    color: var(--pink);
    letter-spacing: 0.5px;
  }
  .contact {
    position: absolute;
    left: 104px;
    font-size: 17px;
    font-weight: 400;
    color: var(--ink);
    letter-spacing: 1px;
    line-height: 1.35;
    white-space: nowrap;
  }
  .contact--address { top: 466px; }
  .contact--phone { top: 560px; }
  .contact--email { top: 598px; }
  .contact--web { top: 636px; }
  .contact__accent { color: var(--orange); }
  .hex--pin { left: 54px; top: 470px; }
  .hex--phone { left: 54px; top: 562px; }
  .hex--mail { left: 54px; top: 600px; }
  .hex--globe { left: 54px; top: 638px; }
  .front-band {
    position: absolute;
    left: 0; right: 0; bottom: 0;
    height: 30px;
    background: var(--band);
  }

  /* Back */
  .back-pattern {
    position: absolute;
    inset: 0;
    background:
      radial-gradient(ellipse 70% 45% at 85% 12%, rgba(236,110,180,0.55) 0%, rgba(236,110,180,0) 70%),
      radial-gradient(ellipse 60% 40% at 30% 30%, rgba(180,40,130,0.35) 0%, rgba(180,40,130,0) 75%),
      radial-gradient(ellipse 80% 50% at 15% 90%, rgba(122,22,86,0.75) 0%, rgba(122,22,86,0) 75%),
      radial-gradient(ellipse 60% 40% at 70% 75%, rgba(142,26,100,0.5) 0%, rgba(142,26,100,0) 75%),
      linear-gradient(165deg, var(--magenta-light) 0%, var(--magenta) 40%, #b8157c 70%, var(--magenta-deep) 100%);
  }
  .back-brand {
    position: absolute;
    right: 44px;
    top: 520px;
    display: flex;
    align-items: center;
    gap: 10px;
  }
  .back-brand__dot { width: 16px; height: 16px; background: #ffffff; }
  .back-brand__name {
    font-size: 30px;
    font-weight: 600;
    line-height: 1;
    color: #ffffff;
  }
</style>
</head>
<body>

  <section class="card card--front" aria-label="Business card front">
    <div class="brand-mark">
      <span class="brand-mark__dot"></span>
      <span class="brand-mark__name">Q7 Funding</span>
    </div>

    <div class="timeline"></div>

    <svg class="hex hex--person" width="46" height="46" viewBox="0 0 46 46" aria-hidden="true">
      <polygon points="23,1 43,12 43,34 23,45 3,34 3,12" fill="var(--green)"/>
      <circle cx="23" cy="18" r="6" fill="#fff"/>
      <path d="M12 33 C13 25 33 25 34 33 Z" fill="#fff"/>
    </svg>
    <h1 class="person-name"><span class="person-name__first">DORIAN</span> <span class="person-name__last">VALE</span></h1>
    <p class="person-title">General Manager</p>

    <svg class="hex hex--pin" width="26" height="26" viewBox="0 0 26 26" aria-hidden="true">
      <polygon points="13,1 24,7 24,19 13,25 2,19 2,7" fill="var(--magenta)"/>
      <path d="M13 6 a4 4 0 0 1 4 4 c0 3 -4 8 -4 8 s-4 -5 -4 -8 a4 4 0 0 1 4 -4 z" fill="#fff"/>
      <circle cx="13" cy="10" r="1.5" fill="var(--magenta)"/>
    </svg>
    <p class="contact contact--address">48 Harbor Row,<br>Northfield 12, NF - 20418</p>

    <svg class="hex hex--phone" width="26" height="26" viewBox="0 0 26 26" aria-hidden="true">
      <polygon points="13,1 24,7 24,19 13,25 2,19 2,7" fill="var(--orange)"/>
      <path d="M9 8 l2 -1 l2 3 l-1.5 1.2 c0.6 1.5 1.8 2.7 3.3 3.3 l1.2 -1.5 l3 2 l-1 2 c-4 0 -9 -5 -9 -9 z" fill="#fff"/>
    </svg>
    <p class="contact contact--phone">+014 5520 8163</p>

    <svg class="hex hex--mail" width="26" height="26" viewBox="0 0 26 26" aria-hidden="true">
      <polygon points="13,1 24,7 24,19 13,25 2,19 2,7" fill="var(--band)"/>
      <rect x="7" y="9" width="12" height="8" fill="#fff"/>
      <path d="M7 9 L13 14 L19 9" stroke="var(--band)" stroke-width="1.2" fill="none"/>
    </svg>
    <p class="contact contact--email">hello@q7funding.com</p>

    <svg class="hex hex--globe" width="26" height="26" viewBox="0 0 26 26" aria-hidden="true">
      <polygon points="13,1 24,7 24,19 13,25 2,19 2,7" fill="var(--purple)"/>
      <circle cx="13" cy="13" r="6" fill="none" stroke="#fff" stroke-width="1.3"/>
      <ellipse cx="13" cy="13" rx="2.5" ry="6" fill="none" stroke="#fff" stroke-width="1"/>
      <line x1="7" y1="13" x2="19" y2="13" stroke="#fff" stroke-width="1"/>
    </svg>
    <p class="contact contact--web">www.<span class="contact__accent">q7funding</span>.com</p>

    <div class="front-band"></div>
  </section>

  <section class="card card--back" aria-label="Business card back">
    <div class="back-pattern" role="img" aria-label="Embossed repeating brand pattern in tonal magenta and deep plum covering the card back"></div>
    <div class="back-brand">
      <span class="back-brand__dot"></span>
      <span class="back-brand__name">Q7 Funding</span>
    </div>
  </section>

</body>
</html>
```